Flyer-Design für Brick and Stone Restorator
Zielgruppe
Wir sind Sydneys führender Brick and Stone Restorator.
Aufgabenstellung
Unsere neue webseite geht in ein paar tagen online und wir möchten gerne passenden zur neuen Webseite ein corporate Flyer, letztendlich soll es ein Print Version von unserer neuen Webseite sein. Sprich die wichtigsten Informationen der Webseite soll in dem Flyer enthalten sein. Letztendlich möchte ich designer keine großen einschränkungen geben, weil das ist euer job kreativ sein ;), aber der flyer sollte evtl. so aufgebaut sein das am Ende die leute entweder uns anrufen oder doch auf unsere neue Webseite gehen sprich evtl ein QR- code or what ever.
Unsere Domain ist kestrelvale.com.au, aber damit ihr die neue Webseite schon sehen könnt müsst ihr auf kestrelvale.com.au/ new, falls dieser Link nicht mehr funktionieren sollte, ist sie schon auf der richtigen domain hochgeladen.
Falls ihr irgendwelche Logos Bilder oder sonst was benötigt und diese nicht aus der Webseite entnehmen könnt, schickt einfach eine kurze Naricht, ich beantworte diese so schnell wie möglich ;)
der Flyer soll ein 6 pager sein!!
mit freundlichen Grüßen euer Kestrel Vale Team

```html
<!DOCTYPE html>
<html lang="en">
<head>
<meta charset="utf-8">
<title>Kestrel Vale – Contact Us Panels</title>
<link href="https://fonts.googleapis.com/css2?family=Source+Sans+3:wght@400;600;700&display=swap" rel="stylesheet">
<style>
  :root {
    --stage: #e6e6e4;
    --navy: #211840;
    --tan: #e8d3a2;
    --white: #ffffff;
    --ink: #211840;
    --sky: #cfd4d8;
    --brick: #7a4632;
    --brick-dark: #4e2f24;
    --map-base: #f1f0ec;
    --map-green: #cfe5b8;
  }
  * { margin: 0; padding: 0; box-sizing: border-box; }
  html, body { width: 1200px; height: 857px; overflow: hidden; }
  body {
    background: var(--stage);
    font-family: "Source Sans 3", "Segoe UI", sans-serif;
    position: relative;
  }

  /* panel frame */
  .panel {
    position: absolute;
    top: 207px;
    width: 289px;
    height: 459px;
    background: var(--navy);
    overflow: hidden;
  }
  .panel--card { left: 81px; }
  .panel--icons { left: 492px; }
  .panel--labels { left: 893px; }

  .panel-title {
    position: absolute;
    top: 36px; left: 0; width: 100%;
    text-align: center;
    color: var(--tan);
    font-size: 15px;
    font-weight: 600;
    letter-spacing: 0.3px;
  }
  .panel-photo {
    position: absolute;
    top: 92px; left: 0;
    width: 100%; height: 333px;
    background: linear-gradient(180deg, var(--sky) 0%, #a98873 22%, var(--brick) 45%, #6a3d2c 75%, var(--brick-dark) 100%);
  }
  .panel-photo--shaded {
    background:
      linear-gradient(180deg, rgba(20,14,30,0.15) 0%, rgba(20,14,30,0.45) 40%, rgba(20,14,30,0.2) 100%),
      linear-gradient(180deg, var(--sky) 0%, #a98873 22%, var(--brick) 45%, #6a3d2c 75%, var(--brick-dark) 100%);
  }

  .map {
    position: absolute;
    background:
      radial-gradient(circle at 78% 20%, var(--map-green) 0 16%, transparent 17%),
      radial-gradient(circle at 8% 55%, var(--map-green) 0 8%, transparent 9%),
      var(--map-base);
  }

  /* white contact card (first panel) */
  .card {
    position: absolute;
    top: 23px; left: 23px;
    width: 184px; height: 291px;
    background: var(--white);
    color: var(--ink);
  }
  .card-brand {
    position: absolute;
    top: 16px; left: 0; width: 100%;
    text-align: center;
  }
  .card-list {
    position: absolute;
    top: 67px; left: 12px;
    list-style: none;
  }
  .card-row { position: absolute; left: 0; white-space: nowrap; }
  .card-label { position: absolute; left: 0; font-size: 7.5px; font-weight: 600; }
  .card-value { position: absolute; left: 65px; top: 1px; font-size: 5.6px; line-height: 1.45; }
  .card-map { left: 0; top: 170px; width: 184px; height: 121px; }

  /* brand name */
  .brand-name {
    display: block;
    font-size: 17px;
    font-weight: 700;
    letter-spacing: 0.5px;
    line-height: 1.1;
  }
  .brand-tag {
    display: block;
    font-size: 5px;
    font-weight: 700;
    letter-spacing: 0.6px;
    margin-top: 2px;
  }

  /* overlay layout (second and third panels) */
  .overlay-brand {
    position: absolute;
    top: 33px; left: 0; width: 100%;
    text-align: center;
    color: var(--white);
  }
  .overlay-list {
    position: absolute;
    top: 81px;
    list-style: none;
    color: var(--white);
  }
  .overlay-list--icons { left: 32px; }
  .overlay-list--labels { left: 23px; }
  .overlay-row { position: absolute; left: 0; white-space: nowrap; }
  .overlay-label { position: absolute; left: 0; font-size: 7.6px; }
  .overlay-value { position: absolute; font-size: 7.6px; line-height: 1.1; }
  .overlay-list--icons .overlay-value { left: 31px; }
  .overlay-list--labels .overlay-value { left: 59px; }
  .overlay-map { left: 23px; top: 194px; width: 184px; height: 121px; }

  .icon {
    position: absolute; left: 0; top: -1px;
    width: 11px; height: 11px;
    fill: none; stroke: var(--white); stroke-width: 1.4;
  }
  .icon--solid { fill: var(--white); stroke: none; }
</style>
</head>
<body>

<section class="panel panel--card">
  <h2 class="panel-title">Contact&nbsp; Us</h2>
  <div class="panel-photo" role="img" aria-label="Photograph of a multi-storey red brick heritage building">
    <div class="card">
      <div class="card-brand">
        <span class="brand-name">KESTREL VALE</span>
        <span class="brand-tag">BRICK AND STONE RESTORATION</span>
      </div>
      <ul class="card-list">
        <li class="card-row" style="top:0"><span class="card-label">Phone</span><span class="card-value">0400 555 018</span></li>
        <li class="card-row" style="top:16px"><span class="card-label">Office Hours</span><span class="card-value">Mon – Fri 9am – 5pm</span></li>
        <li class="card-row" style="top:32px"><span class="card-label">E-Mail</span><span class="card-value">enquiries@kestrelvale.com.au</span></li>
        <li class="card-row" style="top:48px"><span class="card-label">Website</span><span class="card-value">www.kestrelvale.com.au</span></li>
        <li class="card-row" style="top:64px"><span class="card-label">Post Address</span><span class="card-value">PO Box 4821, Harlow Bay, NSW 2099</span></li>
        <li class="card-row" style="top:80px"><span class="card-label">Location</span><span class="card-value">12 / 4-6 Fernlea Lane,<br>Ashcombe, NSW 2048, Australia</span></li>
      </ul>
      <div class="map card-map" role="img" aria-label="Street map showing the office location"></div>
    </div>
  </div>
</section>

<section class="panel panel--icons">
  <h2 class="panel-title">Contact Us</h2>
  <div class="panel-photo panel-photo--shaded" role="img" aria-label="Photograph of a multi-storey red brick heritage building">
    <div class="overlay-brand">
      <span class="brand-name">KESTREL VALE</span>
      <span class="brand-tag">BRICK AND STONE RESTORATION</span>
    </div>
    <ul class="overlay-list overlay-list--icons">
      <li class="overlay-row" style="top:0">
        <svg class="icon icon--solid" viewBox="0 0 12 12"><path d="M2.5 1 4.5 3.4 3.4 4.6c.8 1.7 2.2 3.1 3.9 3.9L8.5 7.4 11 9.4 9.6 11C5 10.5 1.4 7 1 2.4Z"/></svg>
        <span class="overlay-value">0400 555 018</span></li>
      <li class="overlay-row" style="top:16px">
        <svg class="icon" viewBox="0 0 12 12"><circle cx="6" cy="6" r="4.8"/><path d="M6 3v3.2l2 1.3"/></svg>
        <span class="overlay-value">Mon – Fri 9am – 5pm</span></li>
      <li class="overlay-row" style="top:32px">
        <svg class="icon icon--solid" viewBox="0 0 12 12"><path d="M1 2.5h10v1L6 6.6 1 3.5Z M1 4.8l5 3 5-3V10H1Z"/></svg>
        <span class="overlay-value">enquiries@kestrelvale.com.au</span></li>
      <li class="overlay-row" style="top:48px">
        <svg class="icon" viewBox="0 0 12 12"><circle cx="6" cy="6" r="4.8"/><ellipse cx="6" cy="6" rx="2" ry="4.8"/><path d="M1.2 6h9.6M2 3.5h8M2 8.5h8"/></svg>
        <span class="overlay-value">www.kestrelvale.com.au</span></li>
      <li class="overlay-row" style="top:64px">
        <svg class="icon" viewBox="0 0 12 12"><path d="M1 5 6 1.5 11 5v5.5H1Z M1 5l5 3.5L11 5 M1 10.5 4.8 7.6 M11 10.5 7.2 7.6"/></svg>
        <span class="overlay-value">PO Box 4821, Harlow Bay, NSW 2099</span></li>
      <li class="overlay-row" style="top:80px">
        <svg class="icon icon--solid" viewBox="0 0 12 12" style="top:1px;height:13px"><path d="M6 .5a4 4 0 0 1 4 4c0 3-4 7.3-4 7.3S2 7.5 2 4.5a4 4 0 0 1 4-4Zm0 2.3a1.7 1.7 0 1 0 0 3.4 1.7 1.7 0 0 0 0-3.4Z"/></svg>
        <span class="overlay-value">12 / 4-6 Fernlea Lane,<br>Ashcombe, NSW 2048, Australia</span></li>
    </ul>
    <div class="map overlay-map" role="img" aria-label="Street map showing the office location"></div>
  </div>
</section>

<section class="panel panel--labels">
  <h2 class="panel-title">Contact Us</h2>
  <div class="panel-photo panel-photo--shaded" role="img" aria-label="Photograph of a multi-storey red brick heritage building">
    <div class="overlay-brand">
      <span class="brand-name">KESTREL VALE</span>
      <span class="brand-tag">BRICK AND STONE RESTORATION</span>
    </div>
    <ul class="overlay-list overlay-list--labels">
      <li class="overlay-row" style="top:0"><span class="overlay-label">Phone</span><span class="overlay-value">0400 555 018</span></li>
      <li class="overlay-row" style="top:16px"><span class="overlay-label">Office Hours</span><span class="overlay-value">Mon – Fri 9am – 5pm</span></li>
      <li class="overlay-row" style="top:32px"><span class="overlay-label">E-Mail</span><span class="overlay-value">enquiries@kestrelvale.com.au</span></li>
      <li class="overlay-row" style="top:48px"><span class="overlay-label">Website</span><span class="overlay-value">www.kestrelvale.com.au</span></li>
      <li class="overlay-row" style="top:64px"><span class="overlay-label">Post Address</span><span class="overlay-value">PO Box 4821, Harlow Bay, NSW 2099</span></li>
      <li class="overlay-row" style="top:80px"><span class="overlay-label">Location</span><span class="overlay-value">12 / 4-6 Fernlea Lane,<br>Ashcombe, NSW 2048, Australia</span></li>
    </ul>
    <div class="map overlay-map" role="img" aria-label="Street map showing the office location"></div>
  </div>
</section>

</body>
</html>
```